Marlo's Bakes Tortehouse LLC website

Artisan cheesecake business looking for excellent talent to design bright, fun, engaging website for our company. We also recently acquired a food truck so we are able to cater and attend food truck events.
Our mission is to create fun, unique, delicious flavors of cheesecake and we bake them in mason jars and whole cheesecakes. We strive to exceed our customers' expectations in everything we do.
Target Market(s)
Foodies, cheesecake lovers, dessert lovers, food truck people,
Industry/Entity Type
Dessert, Catering, Pop Up events, Food truck
Coding
Coded - Design and coding required
Number of Pages Required
4 page
Requirements
Must have
- Pictures of my cheesecakes
Nice to have
- Bright, colorful, eye-catching design with a good flow

```html
<!DOCTYPE html>
<html lang="en">
<head>
<meta charset="utf-8">
<title>Marlo's Bakes Tortehouse LLC</title>
<link rel="stylesheet" href="https://fonts.googleapis.com/css2?family=Anton&family=Dancing+Script:wght@600&family=Tinos:ital,wght@0,400;0,700;1,400;1,700&family=Poppins:wght@400;500;600&display=swap">
<style>
:root{
  --pink:#f7c8cf;
  --pink-deep:#e3a0aa;
  --pink-text:#e6a3ad;
  --rose:#ea9fab;
  --brown:#5d463b;
  --brown-dark:#4e3a30;
  --grey:#e7e7e7;
  --white:#ffffff;
  --ink:#3a2a24;
}
*{margin:0;padding:0;box-sizing:border-box}
html,body{width:1200px;height:4471px;overflow:hidden;background:var(--white)}
body{font-family:"Tinos",serif;color:var(--ink);position:relative}
section,header,footer{position:relative;width:1200px;overflow:hidden}
.abs{position:absolute}
.script{font-family:"Dancing Script",cursive;font-weight:600}
.btn{position:absolute;display:flex;align-items:center;justify-content:center;border-radius:18px;font-family:"Poppins",sans-serif;font-weight:500;font-size:18px;height:35px;width:153px}
.btn-brown{background:var(--brown);color:#f6dde1}
.btn-pink{background:var(--rose);color:var(--brown)}
.section-title{position:absolute;left:0;width:1200px;text-align:center;font-size:46px;line-height:1.2;color:var(--brown)}
.title-rule{position:absolute;left:578px;width:44px;height:2px;background:var(--rose)}
.photo{position:absolute}

.top-strip{height:7px;background:var(--pink)}
.site-header{height:139px;background:var(--white)}
.brand-mark{left:100px;top:28px;width:94px;height:94px;border-radius:50%;background:var(--pink-text);display:flex;align-items:center;justify-content:center;text-align:center;color:var(--white);font-family:"Tinos",serif;font-size:14px;line-height:1.1}
.contact-line{font-size:14px;line-height:18px}
.contact-line .link{color:var(--pink-text);text-decoration:underline}
.follow{left:1025px;top:26px;font-size:10px;color:var(--pink-text)}
.socials{left:1025px;top:44px;display:flex;gap:4px}
.socials span{width:13px;height:13px;background:var(--pink-text);border-radius:2px}
.main-nav{left:0;top:100px;width:1200px}
.main-nav a{position:absolute;font-size:14px;color:var(--ink);text-decoration:none;letter-spacing:.5px}

.hero{height:651px;background:var(--grey)}
.hero-photo{left:573px;top:0;width:627px;height:651px;background:radial-gradient(ellipse at 55% 55%,#f5ecd2 0%,#e8d9b4 35%,#9a7a57 60%,#e4e2df 80%)}
.hero-kicker{left:100px;top:148px;font-size:54px;line-height:1.1;color:var(--brown)}
.hero-big{left:98px;top:206px;font-family:"Anton",sans-serif;font-size:118px;line-height:1;color:var(--pink-text)}
.hero-line{left:100px;top:326px;font-family:"Anton",sans-serif;font-size:60px;line-height:1;color:var(--pink-text)}

.about{height:563px;background:var(--pink)}
.about-photo{left:102px;top:151px;width:410px;height:330px;border-radius:20px;background:linear-gradient(160deg,#c9d8e4 0%,#e6a9bd 40%,#d97fa2 65%,#8e8d8a 100%)}
.about-copy{left:563px;top:170px;width:524px;font-size:12.5px;line-height:16px;text-align:justify;color:var(--ink)}
.about-copy p+p{margin-top:16px}

.events{height:634px;background:var(--white)}
.event{position:absolute;width:320px;height:140px}
.event svg{position:absolute;left:0;top:0}
.event-title{position:absolute;left:106px;top:4px;width:220px;font-size:20px;line-height:22px;color:var(--pink-text);text-transform:uppercase}
.event-desc{position:absolute;left:108px;top:56px;font-size:12px;line-height:15px;color:var(--ink)}
.event-more{position:absolute;left:106px;top:94px;font-size:17px;font-style:italic;font-weight:700;text-decoration:underline;color:var(--brown)}
.dots{left:580px;top:557px;display:flex;gap:6px}
.dots span{width:11px;height:11px;border-radius:50%;border:1.5px solid var(--brown)}
.dots span:first-child{background:var(--brown)}

.small-batch{height:712px;background:var(--brown)}
.small-batch .section-title{color:var(--pink-text)}
.round{position:absolute;width:306px;height:306px;border-radius:50%;border:4px solid var(--rose);top:189px}
.round-label{position:absolute;width:306px;text-align:center;top:525px;font-size:14px;font-weight:700;color:var(--white);letter-spacing:.5px}

.artisan{height:667px;background:var(--white)}
.card{position:absolute;top:232px;width:294px;height:292px;box-shadow:0 2px 5px rgba(0,0,0,.2)}
.card .photo{left:0;top:0;width:100%;height:254px}
.card-label{position:absolute;left:0;bottom:0;width:100%;height:38px;background:var(--pink-deep);display:flex;align-items:center;justify-content:center;font-size:16px;color:var(--brown-dark);letter-spacing:.5px}

.orders{height:635px;background:var(--pink-deep)}
.orders-intro{left:150px;top:173px;width:900px;text-align:center;font-size:12px;line-height:16px;font-style:italic;color:var(--brown)}
.order-col{position:absolute;top:238px;width:440px}
.order-col h3{font-size:38px;line-height:1.1;color:var(--brown);text-decoration:underline;text-decoration-thickness:1px;text-underline-offset:6px}
.order-item{position:absolute;left:0}
.order-item strong{display:block;font-size:25px;line-height:28px;color:var(--brown)}
.order-item em{display:block;font-size:14px;line-height:15px;margin-left:4px;color:var(--brown)}
.orders-divider{left:585px;top:248px;width:2px;height:300px;background:var(--brown)}

.site-footer{height:403px;background:var(--brown);color:var(--white)}
.footer-mark{left:174px;top:51px;width:166px;height:166px;border-radius:50%;background:var(--pink);border:3px solid var(--white);display:flex;align-items:center;justify-content:center;text-align:center;color:var(--white);font-size:24px;line-height:1.1}
.footer-about{left:92px;top:243px;width:330px;text-align:center;font-size:14px;line-height:24px}
.footer-divider{top:94px;width:2px;height:248px;background:#a89088}
.footer-head{top:64px;font-family:"Poppins",sans-serif;font-weight:600;font-size:21px;color:var(--pink-text)}
.quick-links{left:514px;top:132px;list-style:none}
.quick-links li{height:37px;font-size:14px;font-family:"Tinos",serif}
.quick-links li::before{content:"\203A";margin-right:12px}
.contact-row{left:846px;display:flex;align-items:flex-start;gap:26px;font-size:17px;line-height:24px}
.contact-row svg{flex:none;margin-top:3px}
.copyright{height:60px;background:var(--pink);display:flex;align-items:center;justify-content:center;font-family:"Poppins",sans-serif;font-size:12px;color:var(--brown)}
</style>
</head>
<body>

<div class="top-strip"></div>

<header class="site-header">
  <div class="abs brand-mark">Marlo's<br>Bakes</div>
  <div class="abs contact-line" style="left:514px;top:26px">
    <span class="link">&#9742; Order Now 503-555-0142</span><br>
    <span style="margin-left:16px">Local pick up only</span>
  </div>
  <div class="abs contact-line" style="left:770px;top:26px">
    <span class="link">&#9993; Contact Email</span><br>
    <span style="margin-left:16px">Info@yoursite.com</span>
  </div>
  <div class="abs follow">Follow Us</div>
  <div class="abs socials"><span></span><span></span><span></span><span></span></div>
  <nav class="abs main-nav">
    <a style="left:502px">HOME</a>
    <a style="left:592px">MENU</a>
    <a style="left:683px">EVENTS</a>
    <a style="left:787px">ORDER</a>
    <a style="left:891px">ABOUT US</a>
    <a style="left:1009px">CONTACT US</a>
  </nav>
</header>

<section class="hero">
  <div class="photo hero-photo" role="img" aria-label="Slice of coconut-topped cheesecake with whipped cream and chocolate crust"></div>
  <div class="abs hero-kicker script">Cheesecake is</div>
  <div class="abs hero-big">A love</div>
  <div class="abs hero-line">Like no other.</div>
  <a class="btn btn-brown" style="left:99px;top:420px">Order Now</a>
</section>

<section class="about">
  <h2 class="section-title script" style="top:48px">About Us</h2>
  <div class="title-rule" style="top:111px"></div>
  <div class="photo about-photo" role="img" aria-label="The owners standing in front of the pink dessert food truck"></div>
  <div class="abs about-copy">
    <p>consectetur adipiscing elit. Quid autem habent admirationis, cum prope accesseris? An hoc usque quaque, aliter in vita? Non igitur de improbo, sed de callido improbo quaerimus, qualis Q. Nam quibus rebus efficiuntur voluptates, eae non sunt in potestate sapientis. Negare non possum. Huic mori optimum esse propter desperationem sapientiae, illi propter spem vivere. Quid enim me prohiberet Epicureum esse, si probarem, quae ille diceret? . <b>Admirationis, cum prope accesseris? An hoc usque quaque, aliter in vita? Non igitur de improbo, sed de callido improbo quaerimus, qualis Q. Nam quibus rebus efficiuntur voluptates, eae non sunt</b> Huic mori optimum esse propter desperationem sapientiae, illi propter spem vivere. Quid enim me prohiberet Epicureum esse, si probarem, quae ille diceret? Qui-vere falsone, quaerere mittimus-dicitur oculis se privasse;</p>
    <p>potestate sapientis. Negare non possum. Huic mori optimum esse propter desperationem sapientiae, illi propter spem vivere. Quid enim me prohiberet Epicureum esse, si probarem, quae ille diceret? Qui-vere falsone, quaerere mittimus-dicitur oculis se privasse;</p>
  </div>
  <a class="btn btn-brown" style="left:564px;top:429px">Learn More</a>
</section>

<section class="events">
  <h2 class="section-title script" style="top:50px">Events</h2>
  <div class="title-rule" style="top:106px"></div>

  <div class="event" style="left:99px;top:172px">
    <svg width="92" height="92" viewBox="0 0 92 92"><rect x="0" y="10" width="92" height="80" rx="8" fill="#5d463b"/><rect x="18" y="0" width="9" height="20" rx="4.5" fill="#e6a3ad"/><rect x="65" y="0" width="9" height="20" rx="4.5" fill="#e6a3ad"/><rect x="9" y="32" width="74" height="48" rx="3" fill="#f7c8cf"/><text x="46" y="55" text-anchor="middle" font-family="Dancing Script,cursive" font-weight="600" font-size="16" fill="#3a2a24">Monday</text><text x="46" y="72" text-anchor="middle" font-family="Tinos,serif" font-weight="700" font-size="15" fill="#3a2a24">7/4</text></svg>
    <div class="event-title">Effici ntur volup desperationem</div>
    <div class="event-desc">Magnum cognitione dignumam<br>Averuntlectulis plerumque moriun</div>
    <div class="event-more">Read More</div>
  </div>
  <div class="event" style="left:448px;top:172px">
    <svg width="92" height="92" viewBox="0 0 92 92"><rect x="0" y="10" width="92" height="80" rx="8" fill="#5d463b"/><rect x="18" y="0" width="9" height="20" rx="4.5" fill="#e6a3ad"/><rect x="65" y="0" width="9" height="20" rx="4.5" fill="#e6a3ad"/><rect x="9" y="32" width="74" height="48" rx="3" fill="#f7c8cf"/><text x="46" y="55" text-anchor="middle" font-family="Dancing Script,cursive" font-weight="600" font-size="16" fill="#3a2a24">Tuesday</text><text x="46" y="72" text-anchor="middle" font-family="Tinos,serif" font-weight="700" font-size="15" fill="#3a2a24">16/2</text></svg>
    <div class="event-title">Effici ntur volup desperationem</div>
    <div class="event-desc">Magnum cognitione dignumam<br>Averuntlectulis plerumque moriun</div>
    <div class="event-more">Read More</div>
  </div>
  <div class="event" style="left:797px;top:172px">
    <svg width="92" height="92" viewBox="0 0 92 92"><rect x="0" y="10" width="92" height="80" rx="8" fill="#5d463b"/><rect x="18" y="0" width="9" height="20" rx="4.5" fill="#e6a3ad"/><rect x="65" y="0" width="9" height="20" rx="4.5" fill="#e6a3ad"/><rect x="9" y="32" width="74" height="48" rx="3" fill="#f7c8cf"/><text x="46" y="55" text-anchor="middle" font-family="Dancing Script,cursive" font-weight="600" font-size="16" fill="#3a2a24">Friday</text><text x="46" y="72" text-anchor="middle" font-family="Tinos,serif" font-weight="700" font-size="15" fill="#3a2a24">8/5</text></svg>
    <div class="event-title">Effici ntur volup desperationem</div>
    <div class="event-desc">Magnum cognitione dignumam<br>Averuntlectulis plerumque moriun</div>
    <div class="event-more">Read More</div>
  </div>
  <div class="event" style="left:99px;top:364px">
    <svg width="92" height="92" viewBox="0 0 92 92"><rect x="0" y="10" width="92" height="80" rx="8" fill="#5d463b"/><rect x="18" y="0" width="9" height="20" rx="4.5" fill="#e6a3ad"/><rect x="65" y="0" width="9" height="20" rx="4.5" fill="#e6a3ad"/><rect x="9" y="32" width="74" height="48" rx="3" fill="#f7c8cf"/><text x="46" y="55" text-anchor="middle" font-family="Dancing Script,cursive" font-weight="600" font-size="16" fill="#3a2a24">Thursday</text><text x="46" y="72" text-anchor="middle" font-family="Tinos,serif" font-weight="700" font-size="15" fill="#3a2a24">29/4</text></svg>
    <div class="event-title">Effici ntur volup desperationem</div>
    <div class="event-desc">Magnum cognitione dignumam<br>Averuntlectulis plerumque moriun</div>
    <div class="event-more">Read More</div>
  </div>
  <div class="event" style="left:448px;top:364px">
    <svg width="92" height="92" viewBox="0 0 92 92"><rect x="0" y="10" width="92" height="80" rx="8" fill="#5d463b"/><rect x="18" y="0" width="9" height="20" rx="4.5" fill="#e6a3ad"/><rect x="65" y="0" width="9" height="20" rx="4.5" fill="#e6a3ad"/><rect x="9" y="32" width="74" height="48" rx="3" fill="#f7c8cf"/><text x="46" y="55" text-anchor="middle" font-family="Dancing Script,cursive" font-weight="600" font-size="16" fill="#3a2a24">Saturday</text><text x="46" y="72" text-anchor="middle" font-family="Tinos,serif" font-weight="700" font-size="15" fill="#3a2a24">10/4</text></svg>
    <div class="event-title">Effici ntur volup desperationem</div>
    <div class="event-desc">Magnum cognitione dignumam<br>Averuntlectulis plerumque moriun</div>
    <div class="event-more">Read More</div>
  </div>
  <div class="event" style="left:797px;top:364px">
    <svg width="92" height="92" viewBox="0 0 92 92"><rect x="0" y="10" width="92" height="80" rx="8" fill="#5d463b"/><rect x="18" y="0" width="9" height="20" rx="4.5" fill="#e6a3ad"/><rect x="65" y="0" width="9" height="20" rx="4.5" fill="#e6a3ad"/><rect x="9" y="32" width="74" height="48" rx="3" fill="#f7c8cf"/><text x="46" y="55" text-anchor="middle" font-family="Dancing Script,cursive" font-weight="600" font-size="16" fill="#3a2a24">Sunday</text><text x="46" y="72" text-anchor="middle" font-family="Tinos,serif" font-weight="700" font-size="15" fill="#3a2a24">25/4</text></svg>
    <div class="event-title">Effici ntur volup desperationem</div>
    <div class="event-desc">Magnum cognitione dignumam<br>Averuntlectulis plerumque moriun</div>
    <div class="event-more">Read More</div>
  </div>

  <div class="abs dots"><span></span><span></span><span></span></div>
</section>

<section class="small-batch">
  <h2 class="section-title script" style="top:60px">Small Batch Cheese cakes</h2>
  <div class="round" style="left:99px;background:radial-gradient(circle,#f3e6d6 0%,#e7c9a8 40%,#c9483f 70%,#3b2b24 100%)" role="img" aria-label="Strawberry cheesecakes baked in mason jars"></div>
  <div class="round-label" style="left:99px">LAELIUS CLAMORES</div>
  <div class="round" style="left:446px;background:radial-gradient(circle,#f6e39a 0%,#efd57a 45%,#f3ecd6 70%,#2a2420 100%)" role="img" aria-label="Slice of lemon cheesecake with lemon wedges"></div>
  <div class="round-label" style="left:446px">TURPIUS PROPTER</div>
  <div class="round" style="left:793px;background:radial-gradient(circle,#6a3b28 0%,#4a2618 50%,#efe9e4 72%,#1c1714 100%)" role="img" aria-label="Chocolate-glazed cheesecake topped with raspberries"></div>
  <div class="round-label" style="left:793px">DEMOCRITEUM</div>
  <a class="btn btn-pink" style="left:519px;top:611px">More Cake</a>
</section>

<section class="artisan">
  <h2 class="section-title script" style="top:100px">Artisan Cheesecakes</h2>
  <div class="title-rule" style="top:160px"></div>
  <svg class="abs" style="left:50px;top:308px" width="30" height="70" viewBox="0 0 30 70"><path d="M27 2 L3 35 L27 68" fill="none" stroke="#3a2a24" stroke-width="2"/></svg>
  <svg class="abs" style="left:1128px;top:308px" width="30" height="70" viewBox="0 0 30 70"><path d="M3 2 L27 35 L3 68" fill="none" stroke="#3a2a24" stroke-width="2"/></svg>
  <div class="card" style="left:99px">
    <div class="photo" style="background:radial-gradient(circle,#f4d3b0 0%,#e25a45 40%,#c8322a 60%,#ffffff 80%)" role="img" aria-label="Whole cheesecake topped with sliced strawberries"></div>
    <div class="card-label">TURPIUS PROPTER</div>
  </div>
  <div class="card" style="left:455px;box-shadow:none">
    <div class="photo" style="background:radial-gradient(circle,#d9d9d9 0%,#3a2a24 25%,#2b1d17 50%,#c9c9c9 75%)" role="img" aria-label="Heart-shaped chocolate cheesecake"></div>
    <div class="card-label">DEMOCRITEUM</div>
  </div>
  <div class="card" style="left:806px;box-shadow:none">
    <div class="photo" style="background:radial-gradient(ellipse at 50% 45%,#7a4a2c 0%,#4b2c1c 45%,#2a1c15 70%,#d9d4cf 100%)" role="img" aria-label="Chocolate cheesecake decorated with autumn pumpkins and frosting"></div>
    <div class="card-label">LAELIUS CLAMORES</div>
  </div>
</section>

<section class="orders">
  <h2 class="section-title script" style="top:80px">Orders</h2>
  <p class="abs orders-intro">Honestius nec turpi turpius. Tria genera bonorum Ruid iudicant sensus Suae qui nihil umquam magnumhenestius nec turpi turpiusbonorumiudicant onestius nec Verum tamen cum de rebus grandioribus dicas, ipsae res verba rapiunt; Hoc non est positum in nostra actione. Quod ea non occurrentia</p>

  <div class="order-col" style="left:104px">
    <h3 class="script">Ordering Process</h3>
    <div class="order-item" style="top:68px"><strong>Respondeat totidem ,$18</strong><em>PotestConsequens voluptatibus quibusdam voluptatibus</em></div>
    <div class="order-item" style="top:141px"><strong>Nodeatespo totidem ,$56</strong><em>PotestConsequens voluptatibus quibusdam voluptatibus</em></div>
    <div class="order-item" style="top:205px"><strong>Pondeat totidem ,$78</strong><em>PotestConsequens voluptatibus quibusdam voluptatibus</em></div>
    <div class="order-item" style="top:273px"><strong>Sepondeat totidem ,$21</strong><em>PotestConsequens voluptatibus quibusdam voluptatibus</em></div>
  </div>

  <div class="abs orders-divider"></div>

  <div class="order-col" style="left:728px">
    <h3 class="script">Payment Options</h3>
    <div class="order-item" style="top:68px"><strong>Respondeat totidem ,$18</strong><em>PotestConsequens voluptatibus quibusdam voluptatibus</em></div>
    <div class="order-item" style="top:141px"><strong>Nodeatespo totidem ,$56</strong><em>PotestConsequens voluptatibus quibusdam voluptatibus</em></div>
    <div class="order-item" style="top:205px"><strong>Pondeat totidem ,$78</strong><em>PotestConsequens voluptatibus quibusdam voluptatibus</em></div>
    <div class="order-item" style="top:273px"><strong>Sepondeat totidem ,$21</strong><em>PotestConsequens voluptatibus quibusdam voluptatibus</em></div>
  </div>
</section>

<footer class="site-footer">
  <div class="abs footer-mark">Marlo's<br>Bakes</div>
  <p class="abs footer-about">Lorem ipsum dolor sit amet, consectetur adipiscing elit. Quid autem habent admirationis, cum prope accesseris? An hoc usque quaque, aliter</p>
  <div class="abs footer-divider" style="left:462px"></div>
  <div class="abs footer-divider" style="left:759px"></div>

  <div class="abs footer-head" style="left:493px">Quick Links</div>
  <div class="abs" style="left:493px;top:102px;width:212px;height:1px;background:#d8c4bf"></div>
  <ul class="abs quick-links">
    <li>Home</li><li>Menu</li><li>Events</li><li>About</li><li>Order Now</li><li>Contact</li>
  </ul>

  <div class="abs footer-head" style="left:832px">Contact Informations</div>
  <div class="abs contact-row" style="top:134px">
    <svg width="20" height="28" viewBox="0 0 20 28"><path d="M10 1C5 1 1 5 1 10c0 7 9 17 9 17s9-10 9-17c0-5-4-9-9-9z" fill="#f7c8cf"/><circle cx="10" cy="10" r="3.5" fill="#5d463b"/></svg>
    <span style="font-size:14px;line-height:24px">418 Willow Crest Road<br>Portland, Oregon 97205</span>
  </div>
  <div class="abs contact-row" style="top:227px">
    <svg width="20" height="20" viewBox="0 0 20 20"><path d="M4 1l4 4-2 3c1 3 3 5 6 6l3-2 4 4-3 3C9 19 1 11 1 4z" fill="#f7c8cf"/></svg>
    <span>503-555-0142</span>
  </div>
  <div class="abs contact-row" style="top:257px">
    <svg width="20" height="16" viewBox="0 0 20 16"><rect x="0" y="1" width="20" height="14" rx="2" fill="#f7c8cf"/><path d="M1 2l9 7 9-7" fill="none" stroke="#5d463b" stroke-width="1.5"/></svg>
    <span>marlosbakes-example.com</span>
  </div>
  <div class="abs contact-row" style="top:287px">
    <svg width="20" height="20" viewBox="0 0 20 20"><circle cx="10" cy="10" r="9" fill="#f7c8cf"/></svg>
    <span>@marlosbakesdesserts</span>
  </div>
  <div class="abs contact-row" style="top:317px">
    <svg width="20" height="20" viewBox="0 0 20 20"><circle cx="10" cy="10" r="9" fill="#f7c8cf"/></svg>
    <span>@marlos bakes</span>
  </div>
</footer>

<div class="copyright">Copyright &copy; 2022 marlosbakes-example.com. All Right Reserved</div>

</body>
</html>
```